Cindermoor Larder Logo/Label Design

I am designing a blueberry label that will be placed on clam shells when the fruit is packed. The label will the company name "The Cindermoor Larder". It will also list Blueberries/Bleuets (Blueberries in French). It small print it would say Dist. By/Par The Cindermoor Larder, Fernhollow, GA 39724 USA. It would also list the package size. 1 US Dry Pint/1 Chopine Seche US 551 ml. I have provided some sample labels that other marketers use.

```html
<!DOCTYPE html>
<html lang="en">
<head>
<meta charset="utf-8">
<title>The Cindermoor Larder – Blueberries Label</title>
<link href="https://fonts.googleapis.com/css2?family=Montserrat:wght@600;700;800&display=swap" rel="stylesheet">
<style>
  :root {
    --navy-frame: #3f4680;
    --navy-band: #474a8a;
    --navy-text: #2e2f6b;
    --lavender-field: #e6e4f1;
    --lavender-disc: #a29dc6;
    --berry-deep: #3a3d86;
    --berry-mid: #6a6cb0;
    --paper: #ffffff;
    --white: #ffffff;
  }
  html, body {
    margin: 0;
    padding: 0;
    width: 1200px;
    height: 840px;
    overflow: hidden;
    background: var(--paper);
  }
  .label {
    display: block;
    width: 1200px;
    height: 840px;
    font-family: "Montserrat", Arial, sans-serif;
  }
  .frame-outer { fill: var(--navy-frame); }
  .frame-inner { fill: var(--lavender-field); }
  .ribbon-tab { fill: var(--navy-frame); }
  .ribbon-band { fill: var(--navy-band); }
  .brand-disc { fill: var(--lavender-disc); }
  .brand-name {
    fill: var(--navy-band);
    font-weight: 800;
    font-size: 44px;
    letter-spacing: 3px;
  }
  .product-title {
    fill: var(--white);
    font-weight: 800;
    font-size: 138px;
    letter-spacing: 6px;
  }
  .size-text {
    fill: var(--navy-text);
    font-weight: 600;
    font-size: 44px;
    letter-spacing: -0.5px;
  }
  .size-volume {
    fill: var(--navy-text);
    font-weight: 700;
    font-size: 46px;
    letter-spacing: -1px;
  }
  .size-rule { stroke: var(--navy-band); stroke-width: 5; }
  .distributor {
    fill: var(--navy-text);
    font-weight: 600;
    font-size: 19px;
    letter-spacing: 0.3px;
  }
</style>
</head>
<body>
<svg class="label" viewBox="0 0 2300 1610" xmlns="http://www.w3.org/2000/svg">
  <defs>
    <radialGradient id="berry-fill" cx="50%" cy="55%" r="60%">
      <stop offset="0%" stop-color="var(--berry-mid)"/>
      <stop offset="70%" stop-color="var(--berry-deep)"/>
      <stop offset="100%" stop-color="var(--lavender-field)" stop-opacity="0"/>
    </radialGradient>
    <path id="brand-arc" d="M 902 475 A 240 240 0 0 1 1382 475"/>
    <path id="distributor-arc" d="M 775 1226 A 460 460 0 0 0 1525 1226"/>
  </defs>

  <!-- Ribbon ends -->
  <path class="ribbon-tab" d="M 320 638 L 440 638 L 440 948 L 320 948 Q 305 948 300 930 L 282 860 Q 272 790 282 720 L 300 655 Q 305 638 320 638 Z"/>
  <path class="ribbon-tab" d="M 1980 630 L 1855 630 L 1855 942 L 1980 942 Q 1995 942 2000 925 L 2015 850 Q 2025 785 2015 720 L 2000 648 Q 1995 630 1980 630 Z"/>

  <!-- Badge frame -->
  <path class="frame-outer" d="M 750 290 Q 930 118 1150 118 Q 1370 118 1545 290 L 1725 290 Q 1855 290 1855 430 L 1855 1180 Q 1855 1315 1725 1315 L 1545 1315 Q 1370 1490 1150 1490 Q 930 1490 750 1315 L 585 1315 Q 440 1315 440 1180 L 440 430 Q 440 290 585 290 Z"/>
  <path class="frame-inner" d="M 772 333 Q 940 162 1150 162 Q 1360 162 1525 333 L 1710 333 Q 1812 333 1812 440 L 1812 1170 Q 1812 1272 1710 1272 L 1525 1272 Q 1360 1446 1150 1446 Q 940 1446 772 1272 L 590 1272 Q 483 1272 483 1170 L 483 440 Q 483 333 590 333 Z"/>

  <!-- Brand -->
  <g class="brand">
    <text class="brand-name">
      <textPath href="#brand-arc" startOffset="50%" text-anchor="middle">THE CINDERMOOR LARDER</textPath>
    </text>
    <circle class="brand-disc" cx="1142" cy="410" r="100"/>
  </g>

  <!-- Title band -->
  <rect class="ribbon-band" x="410" y="560" width="1477" height="337"/>

  <!-- Fruit illustration area -->
  <g role="img" aria-label="Illustration of three glossy blueberries with green leaves">
    <ellipse cx="1120" cy="1090" rx="340" ry="250" fill="url(#berry-fill)"/>
  </g>

  <text class="product-title" x="1150" y="700" text-anchor="middle">BLUEBERRIES</text>
  <text class="product-title" x="1150" y="838" text-anchor="middle">BLUETS</text>

  <!-- Pack size, English -->
  <g class="size-block">
    <text class="size-text" x="652" y="1015" text-anchor="middle">1 US</text>
    <text class="size-text" x="652" y="1060" text-anchor="middle">DRY PINT</text>
    <line class="size-rule" x1="596" y1="1090" x2="716" y2="1090"/>
    <text class="size-volume" x="652" y="1150" text-anchor="middle">551 ml</text>
  </g>

  <!-- Pack size, French -->
  <g class="size-block">
    <text class="size-text" x="1622" y="1015" text-anchor="middle">1 CHOPINE</text>
    <text class="size-text" x="1622" y="1060" text-anchor="middle">SECHE</text>
    <line class="size-rule" x1="1566" y1="1088" x2="1686" y2="1088"/>
    <text class="size-volume" x="1625" y="1150" text-anchor="middle">551 ml</text>
  </g>

  <!-- Distributor line -->
  <text class="distributor">
    <textPath href="#distributor-arc" startOffset="50%" text-anchor="middle">DIST. BY/PAR: THE CINDERMOOR LARDER, FERNHOLLOW, GA 39724 USA</textPath>
  </text>
</svg>
</body>
</html>
```